Business card

We need a business card design for our company based in Auckland , New Zealand called 'Kestrel + Design Ltd'. We provide architectural services. We would like to see designs that use the max. three colours (such as white, black, grey) The final design should communicate financial safety and growth."
Also I will provide our company logo. I would like to the logo to be embeded onto our business card.

Target Market(s)

new residential house, alteration & addition & light commericila design & drafting service

Industry/Entity Type

Architecture

Contact Information for Business Card

Company name: kestrel + design Ltd.
Name: Mark Telford
Job title: architectural designer & Design RQC
email address: mark@kdstudio.co.nz
mobile number: 02 5319 6620
web site: www.kdstudio.co.nz

Requirements
Must have
• My project must have..
• - embeded logo (attached company logo)
• I don't have a bigger version for our company logo, but I have one old one, so you can remove the word from it)
• - insert the attached small PDGQ logo & RQC logo
• - creative, simple and clear business card.
• - Max. three colours
Nice to have
• - Here are the samples I would like to share with you: http://www.velmorindex.com/blog/minimalistic-business-card-designs/
• I would like to have my business card like one of the creation.
Should not have
• TBA

```html
<!DOCTYPE html>
<html lang="en">
<head>
<meta charset="utf-8">
<title>Kestrel + Design Ltd. — Business Card</title>
<link rel="stylesheet" href="https://fonts.googleapis.com/css2?family=Figtree:wght@400;500;700&display=swap">
<style>
  :root {
    --page: #ffffff;
    --card-front: #51524b;
    --card-back: #000000;
    --ink-light: #ffffff;
    --ink-dark: #111111;
    --icon-grey: #6b6b6b;
    --rule: #4a4a4a;
    --badge-light: #e9e9e9;
    --badge-grey: #5a5a55;
  }
  * { margin: 0; padding: 0; box-sizing: border-box; }
  html, body {
    width: 1200px; height: 1192px; overflow: hidden;
    background: var(--page);
    font-family: "Figtree", sans-serif;
  }
  .canvas { position: relative; width: 1200px; height: 1192px; }

  .card {
    position: absolute; left: 262px; width: 677px; height: 394px;
    border-radius: 13px;
  }
  .card--front { top: 143px; background: var(--card-front); }
  .card--back { top: 617px; background: var(--card-back); }

  .brand-mark {
    position: absolute; left: 308px; top: 135px;
    width: 62px; height: 62px; border-radius: 50%;
    background: var(--ink-dark);
  }
  .brand-name {
    position: absolute; left: 0; right: 0; top: 262px;
    text-align: center; color: var(--ink-light);
    font-weight: 700; font-size: 32px; letter-spacing: -0.6px;
  }

  .badge { position: absolute; }
  .badge--licence {
    left: 50px; top: 231px; width: 92px; height: 92px;
    border-radius: 50%; background: var(--badge-light);
    border: 3px solid var(--ink-light);
  }
  .badge--membership {
    left: 168px; top: 241px; width: 102px; height: 74px;
    border-radius: 4px; background: var(--badge-grey);
  }

  .holder {
    position: absolute; left: 384px; top: 126px; color: var(--ink-light);
  }
  .holder__name { font-weight: 700; font-size: 22px; letter-spacing: -0.3px; }
  .holder__role { margin-top: 8px; font-size: 15.5px; font-weight: 400; }
  .holder__rule {
    position: absolute; left: 390px; top: 203px; width: 234px; height: 1px;
    background: var(--rule);
  }

  .contact { position: absolute; left: 344px; top: 220px; list-style: none; }
  .contact__item {
    display: flex; align-items: center; height: 36px;
    color: var(--ink-light); font-size: 22px; letter-spacing: -0.4px;
  }
  .contact__icon { width: 26px; height: 22px; margin-right: 14px; flex: none; }
</style>
</head>
<body>
<main class="canvas">

  <section class="card card--front" aria-label="Card front">
    <div class="brand-mark"></div>
    <p class="brand-name">Kestrel + Design Ltd.</p>
  </section>

  <section class="card card--back" aria-label="Card back">
    <div class="badge badge--licence" role="img" aria-label="Licensed practitioner badge"></div>
    <div class="badge badge--membership" role="img" aria-label="Professional membership badge"></div>

    <div class="holder">
      <p class="holder__name">Mark Telford</p>
      <p class="holder__role">architectural designer &amp; Design RQC</p>
    </div>
    <div class="holder__rule"></div>

    <ul class="contact">
      <li class="contact__item">
        <svg class="contact__icon" viewBox="0 0 26 22" aria-hidden="true">
          <circle cx="12" cy="11" r="10" fill="none" stroke="var(--icon-grey)" stroke-width="1.6"/>
          <path d="M10 5 q-3 6 0 12" fill="none" stroke="var(--icon-grey)" stroke-width="2.4" stroke-linecap="round"/>
        </svg>
        02 5319 6620
      </li>
      <li class="contact__item">
        <svg class="contact__icon" viewBox="0 0 26 22" aria-hidden="true">
          <rect x="1" y="3" width="24" height="16" fill="var(--icon-grey)"/>
          <path d="M1 3 L13 13 L25 3 M1 19 L10 11 M25 19 L16 11" fill="none" stroke="#000" stroke-width="1.4"/>
        </svg>
        mark@kdstudio.co.nz
      </li>
      <li class="contact__item">
        <svg class="contact__icon" viewBox="0 0 26 22" aria-hidden="true">
          <g fill="none" stroke="var(--icon-grey)" stroke-width="1.5">
            <circle cx="12" cy="11" r="10"/>
            <ellipse cx="12" cy="11" rx="4.5" ry="10"/>
            <path d="M2 11 H22 M4 5.5 H20 M4 16.5 H20"/>
          </g>
        </svg>
        www.kdstudio.co.nz
      </li>
    </ul>
  </section>

</main>
</body>
</html>
```